Clay Sparrow- Hand made fashion accessories

Clay sparrow is a new business that will be selling hand made fashion accessories for women such as bags, baskets, knecklaces etc. The items are all hand made from Africa. I would like natural colors leaning more to the cardboard rustic look. I would like the card to look simple but elegant at the same time.

Industry/Entity Type

Business

Contact Information for Business Card

www.claysparrow-example.com.au
sales@claysparrow-example.com.au
Tel: 0452867310

Font styles to use
Decorative
Script

Requirements
Must have
• Earthy and rustic colours. Straw, cardboard etc. Fine black cursive print. One side of card only name
• second side website, email and tel.
Should not have
• No need to have any description of what business sells or does. No pictures of anything.

```html
<!DOCTYPE html>
<html lang="en">
<head>
<meta charset="utf-8">
<title>Clay Sparrow – Business Card</title>
<link rel="stylesheet" href="https://fonts.googleapis.com/css2?family=Cormorant+Garamond:wght@500&display=swap">
<style>
  :root {
    --backdrop: #b9a27f;
    --card-cream: #d3d2bd;
    --card-black: #111111;
    --pattern-tone: #2a2a2a;
    --ink: #161616;
    --rule: #0d0d0d;
  }
  * { margin: 0; padding: 0; box-sizing: border-box; }
  html, body {
    width: 1200px;
    height: 1023px;
    overflow: hidden;
    background: var(--backdrop);
  }
  .canvas {
    width: 1200px;
    height: 1023px;
    display: flex;
    flex-direction: column;
    align-items: center;
    justify-content: center;
    gap: 60px;
  }
  .card {
    position: relative;
    width: 590px;
    height: 360px;
    box-shadow: 0 10px 24px rgba(40, 25, 10, 0.35);
    overflow: hidden;
  }
  .card--contact {
    background: var(--card-cream);
    display: flex;
    align-items: center;
    justify-content: center;
  }
  .contact-list {
    list-style: none;
    font-family: "Cormorant Garamond", serif;
    font-weight: 500;
    font-size: 27px;
    line-height: 1.9;
    color: var(--ink);
    letter-spacing: 0.3px;
  }
  .card--reverse {
    background: var(--card-black);
  }
  .reverse-art {
    position: absolute;
    inset: 0;
    width: 100%;
    height: 100%;
  }
  .brand-name {
    position: absolute;
    left: 150px;
    right: 0;
    top: 0;
    bottom: 0;
    display: flex;
    align-items: center;
    justify-content: center;
    font-family: "Cormorant Garamond", serif;
    font-weight: 500;
    font-size: 46px;
    letter-spacing: 2px;
    color: var(--card-cream);
    white-space: nowrap;
  }
</style>
</head>
<body>
  <main class="canvas">
    <section class="card card--contact">
      <ul class="contact-list">
        <li class="contact-phone">0452-867-310</li>
        <li class="contact-web">www.claysparrow-example.com.au</li>
        <li class="contact-email">sales@claysparrow-example.com.au</li>
      </ul>
    </section>

    <section class="card card--reverse">
      <svg class="reverse-art" viewBox="0 0 590 360" xmlns="http://www.w3.org/2000/svg">
        <rect class="reverse-pattern" x="0" y="0" width="590" height="360"
              fill="var(--pattern-tone)" role="img"
              aria-label="Fine dark geometric lattice pattern covering the card"/>
        <polygon class="reverse-corner" points="0,0 150,0 0,230" fill="var(--card-cream)"/>
        <line class="reverse-rule" x1="168" y1="0" x2="18" y2="230"
              stroke="var(--rule)" stroke-width="4"/>
      </svg>
      <h1 class="brand-name">Clay Sparrow</h1>
    </section>
  </main>
</body>
</html>
```